Stationery Set for BRV Company

I need to create full stationery design for my company; Business Cards, Envelops, Letter Heads, Calendar.
In the letter head and Envelops... only contact information and website links.
Our company is a Service Management company with different domains of innovative services including Technology Service Management, Education Services, Outsourcing Management, Events Management.
I need a modern and innovative design specially for the business card. I some transparent designs and I like it, but don't limit your innovation to what I mentioned. Sky is limit for your innovation.

Target Market(s)

Middle East & Africa

Industry/Entity Type

Business Management

Colors
34a7d8
0355a3
85acd3
86cae7
cee9f5
cfdeed
e4daeb
f3f1f8
ecf7fb

Requirements
Must have
• Name, Title, Email, Mobile
Nice to have
• We have multiple locations in USA, KSA, EGY, so I need ideas about how to include all contact details maybe QR / Barcode or something else.
• Please see our locations and contact information: www.ploventa.com
Should not have
• Too much text

```html
<!DOCTYPE html>
<html lang="en">
<head>
<meta charset="utf-8">
<title>BRV Company Stationery Set</title>
<link href="https://fonts.googleapis.com/css2?family=Montserrat:wght@500;600;700&family=Roboto:wght@400;500&display=swap" rel="stylesheet">
<style>
  :root {
    --backdrop: #c4c4c4;
    --paper: #ffffff;
    --brand-blue: #3a69b0;
    --brand-grey: #c2b9b6;
    --ink: #222222;
    --shadow: 0 2px 4px rgba(0,0,0,0.28);
  }
  * { margin: 0; padding: 0; box-sizing: border-box; }
  html, body { width: 1200px; height: 1000px; overflow: hidden; }
  body { background: var(--backdrop); position: relative; font-family: "Roboto", Arial, sans-serif; color: var(--ink); }

  .sheet { position: absolute; background: var(--paper); box-shadow: var(--shadow); overflow: hidden; }
  .card { width: 319px; height: 196px; }
  .card--blue { background: var(--brand-blue); }

  .edge-band { position: absolute; top: 0; bottom: 0; width: 30px; background: var(--brand-blue); }
  .edge-band--left { left: 0; border-radius: 0 15px 15px 0; }
  .edge-band--right { right: 0; border-radius: 15px 0 0 15px; }
  .edge-band--grey { background: var(--brand-grey); }

  .wordmark { position: absolute; font-family: "Montserrat", Arial, sans-serif; font-weight: 700; color: var(--brand-blue); white-space: nowrap; display: flex; align-items: center; gap: 6px; }
  .wordmark--white { color: #ffffff; }

  .person-name { position: absolute; font-family: "Montserrat", Arial, sans-serif; font-weight: 600; font-size: 13px; color: var(--brand-blue); white-space: nowrap; }
  .person-title { display: block; font-family: "Roboto", Arial, sans-serif; font-weight: 500; font-size: 8px; color: var(--ink); margin-top: 1px; }

  .divider { position: absolute; width: 1px; background: var(--brand-blue); }

  .contacts { position: absolute; font-size: 10px; line-height: 12.5px; white-space: nowrap; }
  .contacts .row { display: flex; align-items: center; gap: 4px; }
  .contacts .gap { height: 7px; }
  .contacts .address { color: var(--brand-blue); }
  .icon { width: 7px; height: 7px; flex: none; }

  .letterhead { left: 118px; top: 480px; width: 380px; height: 490px; }
  .letter-footer { position: absolute; left: 34px; bottom: 21px; display: flex; gap: 16px; font-size: 4.5px; color: #444; white-space: nowrap; }
  .letter-footer span { display: flex; align-items: center; gap: 2px; }
  .letter-footer .icon { width: 4px; height: 4px; }

  .envelope { width: 467px; height: 206px; }
  .return-address { position: absolute; left: 16px; top: 50px; font-size: 5px; line-height: 6.5px; color: var(--ink); }
</style>
</head>
<body>

<section class="sheet card" style="left:46px; top:25px;">
  <div class="edge-band edge-band--left"></div>
  <div class="person-name" style="left:47px; top:56px;">Dana Ruiz<span class="person-title">Director</span></div>
  <div class="divider" style="left:160px; top:58px; height:112px;"></div>
  <div class="contacts" style="left:175px; top:80px;">
    <div class="row"><svg class="icon" viewBox="0 0 8 8"><rect x="2" y="0" width="4" height="8" rx="1" fill="var(--brand-blue)"/></svg>+123 456 7890</div>
    <div class="row"><svg class="icon" viewBox="0 0 8 8"><path d="M0 3h8v5H0z M1 0h6v2H1z" fill="var(--brand-blue)"/></svg>+123 456 7890</div>
    <div class="gap"></div>
    <div class="row"><svg class="icon" viewBox="0 0 8 8"><rect y="1" width="8" height="6" fill="var(--brand-blue)"/></svg>info@emailiddomain.com</div>
    <div class="row"><svg class="icon" viewBox="0 0 8 8"><circle cx="4" cy="4" r="3.5" fill="var(--brand-blue)"/></svg>www.websitedomain.com</div>
    <div class="gap"></div>
    <div class="address">1 King Street, Hochland Park</div>
    <div class="address">City Name, Country 9000</div>
  </div>
</section>

<section class="sheet card" style="left:446px; top:25px;">
  <div class="wordmark" style="left:28px; top:124px; font-size:15px;">BRV Company</div>
  <div class="edge-band edge-band--right"></div>
</section>

<section class="sheet card card--blue" style="left:848px; top:25px;">
  <div class="wordmark wordmark--white" style="left:44px; top:78px; font-size:28px;">BRV Company</div>
</section>

<section class="sheet card" style="left:46px; top:260px;">
  <div class="edge-band edge-band--left"></div>
  <div class="person-name" style="left:118px; top:33px;">Dana Ruiz<span class="person-title">Director</span></div>
  <div class="contacts" style="left:117px; top:80px;">
    <div class="row"><svg class="icon" viewBox="0 0 8 8"><rect x="2" y="0" width="4" height="8" rx="1" fill="var(--brand-blue)"/></svg>+123 456 7890</div>
    <div class="row"><svg class="icon" viewBox="0 0 8 8"><path d="M0 3h8v5H0z M1 0h6v2H1z" fill="var(--brand-blue)"/></svg>+123 456 7890</div>
    <div class="gap"></div>
    <div class="row"><svg class="icon" viewBox="0 0 8 8"><rect y="1" width="8" height="6" fill="var(--brand-blue)"/></svg>info@emailiddomain.com</div>
    <div class="row"><svg class="icon" viewBox="0 0 8 8"><circle cx="4" cy="4" r="3.5" fill="var(--brand-blue)"/></svg>www.websitedomain.com</div>
    <div class="gap"></div>
    <div class="address">1 King Street, Hochland Park</div>
    <div class="address">City Name, Country 9000</div>
  </div>
</section>

<section class="sheet card" style="left:446px; top:260px;">
  <div class="wordmark" style="left:20px; top:122px; font-size:15px;">BRV Company</div>
  <div class="divider" style="left:160px; top:25px; height:155px;"></div>
  <div class="person-name" style="left:175px; top:28px;">Dana Ruiz<span class="person-title">Director</span></div>
  <div class="contacts" style="left:175px; top:82px;">
    <div class="row"><svg class="icon" viewBox="0 0 8 8"><rect x="2" y="0" width="4" height="8" rx="1" fill="var(--brand-blue)"/></svg>+123 456 7890</div>
    <div class="row"><svg class="icon" viewBox="0 0 8 8"><path d="M0 3h8v5H0z M1 0h6v2H1z" fill="var(--brand-blue)"/></svg>+123 456 7890</div>
    <div class="gap"></div>
    <div class="row"><svg class="icon" viewBox="0 0 8 8"><rect y="1" width="8" height="6" fill="var(--brand-blue)"/></svg>info@marlowconsult.com</div>
    <div class="row"><svg class="icon" viewBox="0 0 8 8"><circle cx="4" cy="4" r="3.5" fill="var(--brand-blue)"/></svg>www.marlowconsult.com</div>
    <div class="gap"></div>
    <div class="address">1 King Street, Hochland Park</div>
    <div class="address">City Name, Country 9000 9000</div>
  </div>
</section>

<section class="sheet card" style="left:847px; top:258px;">
  <div class="wordmark" style="left:58px; top:82px; font-size:25px;">BRV Company</div>
</section>

<section class="sheet letterhead">
  <div class="wordmark" style="left:148px; top:20px; font-size:11px;">BRV Company</div>
  <div class="edge-band edge-band--right edge-band--grey" style="top:280px; width:22px;"></div>
  <footer class="letter-footer">
    <span><svg class="icon" viewBox="0 0 8 8"><path d="M0 3h8v5H0z M1 0h6v2H1z" fill="var(--brand-blue)"/></svg>+123 456 7890</span>
    <span><svg class="icon" viewBox="0 0 8 8"><rect y="1" width="8" height="6" fill="var(--brand-blue)"/></svg>info@marlowconsult.com</span>
    <span><svg class="icon" viewBox="0 0 8 8"><circle cx="4" cy="4" r="3.5" fill="var(--brand-blue)"/></svg>www.marlowconsult.com</span>
    <span>| 1 King Street, Hochland Park, City Name, Country 9000</span>
  </footer>
</section>

<section class="sheet envelope" style="left:585px; top:510px;">
  <div class="wordmark" style="left:16px; top:14px; font-size:9px;">BRV Company</div>
  <div class="return-address">1 King Street, Hochland Park<br>City Name, Country 9000</div>
  <div class="edge-band edge-band--right edge-band--grey" style="top:62px; width:24px;"></div>
</section>

<section class="sheet envelope" style="left:585px; top:744px;">
  <svg width="467" height="70" viewBox="0 0 467 70" style="position:absolute; left:0; top:0;">
    <path d="M0 0H467L445 50Q438 60 420 58Q233 45 47 58Q29 60 22 50Z" fill="var(--brand-blue)"/>
  </svg>
</section>

</body>
</html>
```